Need Primer (paint) Label Design

THE ATTACHED LABEL/S ARE SOLEY FOR REFERENCE. DO NOT MAKE ME AN INTERIOR PAINT OR CHALK PAINT LABEL. I ONLY NEED A "PRIMER" LABEL. THE ATTACHED INTERIOR PAINT LABEL IS ONLY TO SHOW YOU THE THEME/DESIGN OF OUR OTHER LABELS. THE BLUE LABEL ONLY HAS A DESIGN ASPECT I LIKE (PRIMER ON SIDE). The last four labels are our competitors.
```````````````````````````````````````````````````````````````````````````````````````````````````
We need this label to look professional, sharp, eye catching and modern.
OUR PRIMARY COLORS ARE BLACK AND WHITE. IF YOU INCOPORATE ANOTHER COLOR, SILVER OR GOLD MIGHT BE IDEAL BUT PLEASE DON'T DRIFT TOO FAR.
The attached documents:
1st - Our Logo
2nd - Our chalk paint label (reference). We do not need a chalk paint label.
3rd. A random design example. I like the PRIME on the side running vertically. I think it's a cool design concept.
````````````````````````````````````````````````````````````````````````````````````````````````````
We are going to be using a normal paint can with a metal bail/handle so please use that with you design work
``````````````````````````````````````````````````````````````````````````````````````````````````
Order, in my head:
2743
Coatings
^^ I want this to stand out as well but I don't want it to be the first thing your eye is drawn to. Probably 2nd
Interior/Exterior
Multi - Surface Primer
^^ Want this to stick out and draw your eye so the customer knows what it is immediately
Exceptional Adhesion, Performance, Durability,
Use on Wood, Drywall, Plaster, Stucco, Masonry, Brick, Paneling, Painted Metal, & Properly Prepared Glossy Surfaces & More
35* Lowe Temperature Application (can be on side or small)
100% Acrylic
Low Odor - Low VOC - Soap & Water Clean Up
1 US Gallon - 3.785 L
Feel free to get creative with it!

```html
<!DOCTYPE html>
<html lang="en">
<head>
<meta charset="utf-8">
<title>2743 Coatings – Multi Surface Primer Label</title>
<link rel="stylesheet" href="https://fonts.googleapis.com/css2?family=Bebas+Neue&family=Barlow:wght@500&family=Jost:wght@300;400&display=swap">
<style>
  :root {
    --ink: #050505;
    --paper: #ffffff;
    --shadow: rgba(0, 0, 0, 0.38);
  }
  * { margin: 0; padding: 0; box-sizing: border-box; }
  html, body {
    width: 1200px;
    height: 973px;
    overflow: hidden;
    background: var(--paper);
  }
  .canvas {
    position: relative;
    width: 1200px;
    height: 973px;
    background: var(--paper);
  }
  .label {
    position: absolute;
    left: 118px;
    top: 75px;
    width: 966px;
    height: 846px;
    background: var(--ink);
    box-shadow: 5px 6px 6px var(--shadow);
    color: var(--paper);
    overflow: hidden;
  }
  .block {
    position: absolute;
    text-align: center;
    white-space: nowrap;
  }
  /* brand wordmark */
  .brand-number {
    left: 333px; width: 300px; top: 52px;
    font-family: "Jost", sans-serif;
    font-weight: 300;
    font-size: 100px;
    line-height: 100px;
    letter-spacing: -4px;
    padding-right: -4px;
  }
  .brand-word {
    left: 333px; width: 300px; top: 161px;
    font-family: "Jost", sans-serif;
    font-weight: 300;
    font-size: 34px;
    line-height: 34px;
    letter-spacing: 6px;
    padding-left: 6px;
  }
  /* vertical product name */
  .product-name {
    position: absolute;
    left: 122px;
    top: 499px;
    transform: translate(-50%, -50%) rotate(-90deg);
    font-family: "Jost", sans-serif;
    font-weight: 400;
    font-size: 122px;
    line-height: 1;
    letter-spacing: 69px;
    padding-left: 69px;
    white-space: nowrap;
  }
  .product-type {
    position: absolute;
    left: 203px;
    top: 496px;
    transform: translate(-50%, -50%) rotate(-90deg);
    font-family: "Jost", sans-serif;
    font-weight: 400;
    font-size: 44px;
    line-height: 1;
    letter-spacing: 19.5px;
    padding-left: 19.5px;
    white-space: nowrap;
  }
  /* central white panel */
  .info-panel {
    position: absolute;
    left: 315px;
    top: 213px;
    width: 342px;
    height: 633px;
    background: var(--paper);
    color: var(--ink);
  }
  .use-type {
    left: 0; width: 100%; top: 60px;
    font-family: "Bebas Neue", sans-serif;
    font-size: 46px;
    line-height: 42px;
    letter-spacing: 7px;
    padding-left: 7px;
  }
  .benefits {
    left: 0; width: 100%; top: 238px;
    font-family: "Barlow", sans-serif;
    font-weight: 500;
    font-size: 24px;
    line-height: 37.5px;
  }
  .surfaces {
    left: 0; width: 100%; top: 394px;
    font-family: "Barlow", sans-serif;
    font-weight: 500;
    font-size: 14.5px;
    line-height: 23.6px;
  }
  .volume {
    left: 0; width: 100%; top: 531px;
    font-family: "Bebas Neue", sans-serif;
    font-size: 30px;
    line-height: 28px;
    letter-spacing: 6px;
    padding-left: 6px;
  }
  /* right column */
  .resin {
    left: 752px; width: 150px; top: 284px;
    font-family: "Bebas Neue", sans-serif;
    font-size: 34px;
    line-height: 36px;
    letter-spacing: 5px;
    padding-left: 5px;
  }
  .temperature {
    left: 757px; width: 150px; top: 454px;
    font-family: "Barlow", sans-serif;
    font-weight: 500;
    font-size: 15px;
    line-height: 23.7px;
  }
  .cleanup {
    left: 767px; width: 160px; top: 726px;
    font-family: "Barlow", sans-serif;
    font-weight: 500;
    font-size: 15px;
    line-height: 23.7px;
  }
</style>
</head>
<body>
<div class="canvas">
  <section class="label">
    <div class="block brand-number">2743</div>
    <div class="block brand-word">COATINGS</div>

    <div class="product-name">MULTI</div>
    <div class="product-type">SURFACE PRIMER</div>

    <div class="info-panel">
      <div class="block use-type">INTERIOR<br>EXTERIOR</div>
      <div class="block benefits">Exceptional Adhesion<br>Performance<br>Durability</div>
      <div class="block surfaces">Use on Wood, Drywall, Plaster, Stucco,<br>Masonry, Brick, Paneling, Painted Metal, &amp;<br>Properly Prepared Glossy Surfaces &amp;<br>More</div>
      <div class="block volume">1 US GALLON<br>&nbsp;&nbsp;3.785 L</div>
    </div>

    <div class="block resin">100%<br>ACRYLIC</div>
    <div class="block temperature">35*<br>Lowe<br>Temperature<br>Application</div>
    <div class="block cleanup">Low Odor&nbsp; Low<br>VOC&nbsp; Soap &amp; Water<br>Clean Up</div>
  </section>
</div>
</body>
</html>
```